Snapframe Party Rentals New Business Card*

Need a business card designed for a Photo Booth Hire company.Must look very professional and colorful.A new creative logo would be a bonus. Our current logo is attached on here.

Contact Information for Business Card

Business Name: SNAPFRAME PARTY RENTALS
Contact Person: MARCUS OKAFOR
Mobile: 0491826350
Email: INFO@SNAPFRAMERENTALS.EXAMPLE
Website: WWW.SNAPFRAMERENTALS.EXAMPLE
Facebook: WWW.FACEBOOK.COM/SNAPFRAME.PARTY.RNT

Font styles to use
Serif
Sans Serif
Script

Colors

Designer to choose colors to be used in the design.

Requirements
Must have
• Bonus if the colors match our website.

```html
<!DOCTYPE html>
<html lang="en">
<head>
<meta charset="utf-8">
<title>Snapframe Party Rentals – Business Card</title>
<link rel="stylesheet" href="https://fonts.googleapis.com/css2?family=Cormorant+Garamond:wght@500&family=Roboto:wght@300&family=Roboto+Condensed:wght@700&family=Fredoka:wght@600&display=swap">
<style>
  :root {
    --stage: #2b2b2d;
    --card-white: #ffffff;
    --pattern-light: #f4f4f4;
    --pattern-mid: #e9e9e9;
    --ink: #111111;
    --card-black: #000000;
    --text-light: #f2f2f2;
    --text-soft: #d9d9d9;
  }
  * { margin: 0; padding: 0; box-sizing: border-box; }
  html, body {
    width: 1200px; height: 960px; overflow: hidden;
    background: var(--stage);
  }
  .stage {
    position: relative; width: 1200px; height: 960px;
    display: flex; flex-direction: column; align-items: center; justify-content: center; gap: 40px;
  }
  .card {
    position: relative; width: 700px; height: 400px;
    box-shadow: 0 8px 24px rgba(0,0,0,.45);
    overflow: hidden;
  }
  /* Front */
  .card--front { background: var(--card-white); }
  .front__pattern {
    position: absolute; inset: 0;
    background: linear-gradient(135deg, var(--pattern-light), var(--pattern-mid));
  }
  .front__brand {
    position: absolute; left: 0; right: 0; top: 150px;
    text-align: center;
  }
  .brand-name {
    font-family: "Cormorant Garamond", Georgia, serif;
    font-weight: 500; font-size: 36px; letter-spacing: 2px;
    color: var(--ink);
  }
  .brand-tagline {
    margin-top: 26px;
    font-family: "Fredoka", "Arial Rounded MT Bold", sans-serif;
    font-weight: 600; font-size: 14px; letter-spacing: 1px;
    color: var(--ink);
  }
  /* Back */
  .card--back { background: var(--card-black); }
  .back__name {
    position: absolute; top: 40px; right: 48px;
    font-family: "Roboto Condensed", "Arial Narrow", sans-serif;
    font-weight: 700; font-size: 26px; letter-spacing: .5px;
    color: var(--text-light);
  }
  .contact-list {
    position: absolute; left: 48px; bottom: 40px;
    list-style: none;
    font-family: "Roboto", Arial, sans-serif;
    font-weight: 300; font-size: 18px; line-height: 1.35;
    color: var(--text-soft);
  }
  .contact-list li { display: flex; align-items: center; gap: 10px; }
  .contact-icon { width: 14px; height: 14px; flex: none; }
</style>
</head>
<body>
<main class="stage">
  <section class="card card--front" aria-label="Business card front">
    <div class="front__pattern" role="img" aria-label="Faint repeating pattern of glasses and moustaches"></div>
    <div class="front__brand">
      <p class="brand-name">SNAPFRAME PARTY RENTALS</p>
      <p class="brand-tagline">SNAPFRAME'S MOST AFFORDABLE PHOTO BOOTH HIRE COMPANY</p>
    </div>
  </section>

  <section class="card card--back" aria-label="Business card back">
    <p class="back__name">MARCUS OKAFOR</p>
    <ul class="contact-list">
      <li>
        <svg class="contact-icon" viewBox="0 0 16 16" aria-hidden="true"><path fill="#fff" d="M3.5 1.5l2.5 3-1.5 1.5c.8 1.8 2.2 3.2 4 4l1.5-1.5 3 2.5-1.5 2.5C6.5 13 3 9.5 1 4z"/></svg>
        0491826350
      </li>
      <li>
        <svg class="contact-icon" viewBox="0 0 16 16" aria-hidden="true"><rect x="1" y="3.5" width="14" height="9" fill="#fff"/><path d="M1.5 4l6.5 5 6.5-5" stroke="#000" stroke-width="1.2" fill="none"/></svg>
        info@snapframerentals.example
      </li>
      <li>
        <svg class="contact-icon" viewBox="0 0 16 16" aria-hidden="true"><circle cx="8" cy="8" r="6.5" fill="#fff"/><path d="M1.5 8h13M8 1.5c-3 3-3 10 0 13M8 1.5c3 3 3 10 0 13" stroke="#000" stroke-width="1" fill="none"/></svg>
        www.snapframerentals.example
      </li>
      <li>
        <svg class="contact-icon" viewBox="0 0 16 16" aria-hidden="true"><circle cx="8" cy="8" r="6.5" fill="#fff"/></svg>
        /snapframe.party.rnt
      </li>
    </ul>
  </section>
</main>
</body>
</html>
```